Brackenvale Herons Soccer Club/Duelmark Football Programs needs a flyer for promotions to young students

We are a soccer(football) club based in Melbourne(suburb of Campbellfield) and are running a professional 5 day a week all year round program for kids aged 8 to 18. Our target is to attract approximately 225 kids to our program by the 8th of march this year(4 weeks).
What sets our program apart is our message and mission statement:
- DuelmarkFootball Programs will send players for a European or local Professional trial when they are ready
- Train like a professional 5 days a week all year round
- Proven program over 12 years
- Testimonials on website http://www.brackenvaleherons-qx.com
The message on the flyer needs to be clear and concise.
"Come and try our program FREE for 3 days"
Lorne Habib,Harbourton Rovers 2015/2016 says "..............."
From only $10 a day
Milo Ferrand Reserve cnr Ashgrove and Tulloch Rd Brackenvale
Positions Limited, Register Now.....website..............
Call Rina Obu on 0400918372, Paul Vasko on 0400736154, Peter Stravinou on 0400482690
Example of a flyer uploaded. Can we magnify our message?

Target Market(s)

children and youth aged 8 years to 18 years

Industry/Entity Type

Club

Requirements
Must have
• at least one testimonial
• background image
• clear, concise with no clutter

```html
<!DOCTYPE html>
<html lang="en">
<head>
<meta charset="utf-8">
<title>Brackenvale Herons Soccer Club – Duelmark Football Programs</title>
<link rel="stylesheet" href="https://fonts.googleapis.com/css2?family=League+Gothic&family=Montserrat:wght@500;600;700&family=Playfair+Display:ital@1&display=swap">
<style>
  :root {
    --red: #a51d20;
    --red-bright: #b3201f;
    --white: #ffffff;
    --ink: #1e1e1e;
    --panel: rgba(20, 20, 20, 0.78);
    --grass-top: #7e9a5a;
    --grass-bottom: #5c7a3a;
  }
  * { margin: 0; padding: 0; box-sizing: border-box; }
  html, body { width: 846px; height: 1200px; overflow: hidden; background: var(--white); }
  .flyer { position: relative; width: 846px; height: 1200px; background: var(--white); font-family: "Montserrat", sans-serif; color: var(--ink); }

  .hero { position: absolute; left: 46px; top: 48px; width: 756px; height: 837px; overflow: hidden; }
  .hero-photo {
    position: absolute; inset: 0;
    background:
      radial-gradient(ellipse 40% 50% at 25% 55%, rgba(170, 40, 40, 0.55), transparent 70%),
      radial-gradient(ellipse 35% 55% at 70% 50%, rgba(235, 235, 240, 0.55), transparent 70%),
      linear-gradient(180deg, #a9b8a0 0%, var(--grass-top) 25%, var(--grass-bottom) 100%);
  }

  .club-mark { position: absolute; left: 50%; top: 26px; width: 44px; height: 44px; margin-left: -22px; border-radius: 50%; background: var(--white); }
  .club-name {
    position: absolute; top: 90px; width: 100%; text-align: center; white-space: nowrap;
    font-family: "League Gothic", sans-serif; font-size: 32px; line-height: 34px; letter-spacing: 1.5px; color: var(--white);
  }
  .ribbon { position: absolute; left: 150px; top: 132px; width: 460px; height: 62px; }
  .ribbon-title {
    position: absolute; top: 132px; width: 100%; text-align: center; white-space: nowrap;
    font-family: "League Gothic", sans-serif; font-size: 66px; line-height: 62px; letter-spacing: 3px; color: var(--red);
  }
  .ribbon-tab {
    position: absolute; left: 50%; top: 204px; transform: translateX(-50%); height: 30px; padding: 0 14px;
    background: var(--red); color: var(--white); white-space: nowrap;
    font-size: 13px; font-weight: 500; line-height: 30px; letter-spacing: 0.4px;
  }

  .headline {
    position: absolute; left: 54px; top: 262px; white-space: nowrap;
    font-family: "League Gothic", sans-serif; font-size: 124px; line-height: 108px; letter-spacing: -0.5px;
    color: var(--white); text-transform: uppercase; font-weight: 400;
  }
  .headline .accent { color: var(--red-bright); }
  .headline .line-two { display: block; padding-left: 40px; }

  .benefits {
    position: absolute; left: 0; top: 516px; width: 380px; height: 321px; background: var(--panel);
    padding: 12px 0 0 27px; color: var(--white); text-transform: uppercase;
  }
  .benefit { font-size: 22px; font-weight: 500; line-height: 31px; letter-spacing: -0.4px; white-space: nowrap; }
  .benefit + .benefit { margin-top: 20px; }
  .benefit .accent { color: var(--red-bright); }
  .training-times { margin-top: 18px; font-size: 18px; font-weight: 500; line-height: 24px; }

  .sponsor { position: absolute; right: 42px; top: 516px; color: var(--ink); text-align: right; white-space: nowrap; }
  .sponsor-label { font-size: 15px; font-weight: 600; letter-spacing: 0.3px; }
  .sponsor-name { display: inline-flex; align-items: center; gap: 8px; margin-top: 14px; font-size: 24px; font-weight: 700; }
  .sponsor-name::before { content: ""; width: 16px; height: 16px; border-radius: 50%; background: var(--ink); }

  .testimonial { position: absolute; left: 394px; top: 686px; color: var(--ink); white-space: nowrap; }
  .testimonial-quote { font-family: "Playfair Display", serif; font-style: italic; font-size: 21px; }
  .testimonial-name { margin-top: 10px; font-size: 19px; font-weight: 600; }
  .testimonial-role { margin-top: 12px; font-size: 13px; font-weight: 600; letter-spacing: -0.2px; }

  .offer {
    position: absolute; top: 893px; width: 100%; text-align: center; white-space: nowrap;
    font-family: "League Gothic", sans-serif; font-weight: 400; font-size: 68px; letter-spacing: 1px; color: var(--ink); line-height: 1;
  }
  .offer .accent { color: var(--red); }

  .contact {
    position: absolute; left: 46px; top: 970px; width: 756px; height: 156px; background: var(--red);
    color: var(--white); padding: 12px 27px 0; white-space: nowrap;
  }
  .urgency { display: flex; align-items: center; gap: 10px; }
  .urgency-text { font-family: "Playfair Display", serif; font-style: italic; font-size: 22px; }
  .register { background: var(--white); color: var(--ink); font-size: 19px; font-weight: 500; padding: 0 8px; line-height: 24px; letter-spacing: 0.5px; }
  .visit { margin-top: 6px; font-size: 18px; font-weight: 500; letter-spacing: -0.2px; }
  .visit strong { font-weight: 700; }
  .phones { margin-top: 8px; text-align: center; font-family: "League Gothic", sans-serif; font-size: 25px; line-height: 30px; letter-spacing: 1px; }
  .phones span + span { margin-left: 18px; }
  .address { margin-top: 8px; font-size: 13.5px; font-weight: 500; }

  .disclaimer { position: absolute; left: 46px; top: 1131px; width: 760px; font-size: 11.5px; font-weight: 600; line-height: 15px; color: #000; }
</style>
</head>
<body>
<main class="flyer">
  <section class="hero">
    <div class="hero-photo" role="img" aria-label="Two young soccer players in red and white kits contesting the ball on a grass pitch"></div>

    <div class="club-mark"></div>
    <div class="club-name">BRACKENVALE HERONS</div>
    <svg class="ribbon" viewBox="0 0 460 62" aria-hidden="true">
      <polygon points="0,24 46,18 46,62 6,58 20,42" fill="#ffffff"/>
      <polygon points="460,24 414,18 414,62 454,58 440,42" fill="#ffffff"/>
      <rect x="44" y="0" width="372" height="62" fill="#ffffff"/>
    </svg>
    <div class="ribbon-title">SOCCER CLUB</div>
    <div class="ribbon-tab">DUELMARK FOOTBALL PROGRAMS</div>

    <h1 class="headline">Make your <span class="accent">Soccer</span><span class="line-two">Dream <span class="accent">a reality</span></span></h1>

    <div class="benefits">
      <p class="benefit">Train like the<br>professionals 5 days a<br>week all year round.</p>
      <p class="benefit"><span class="accent">European</span> and local<br><span class="accent">professional trial</span><br>when ready.</p>
      <p class="training-times">Training times<br>Monday to Friday<br>5pm-7pm</p>
    </div>

    <div class="sponsor">
      <p class="sponsor-label">SUPPORTED BY</p>
      <p class="sponsor-name">STRIDEWELL</p>
    </div>

    <blockquote class="testimonial">
      <p class="testimonial-quote">"I wouldn’t be here without you"</p>
      <p class="testimonial-name">Lorne Habib</p>
      <p class="testimonial-role">Coastal League, Harbourton Rovers Seniors 2015</p>
    </blockquote>
  </section>

  <h2 class="offer">COME AND TRY US <span class="accent">FREE</span> FOR 3 DAYS</h2>

  <section class="contact">
    <div class="urgency">
      <p class="urgency-text">Hurry, don’t miss out, limited positions available!</p>
      <span class="register">REGISTER NOW</span>
    </div>
    <p class="visit"><strong>VISIT</strong> www.brackenvaleherons-qx.com or <strong>CALL</strong> to reserve your place now</p>
    <p class="phones"><span>RINA OBU • 0400918372</span><span>PAUL VASKO • 0400736154</span><span>PETER STRAVINOU • 0400482690</span></p>
    <p class="address">Brackenvale Herons Soccer Club, Milo Ferrand Reserve, cnr Ashgrove st and Tulloch rds, Brackenvale</p>
  </section>

  <p class="disclaimer">Disclaimer: only players that have completed the DuelmarkFootball Program and deemed “ready”, “complete” by the coaching director will be eligible for European and local professional trials</p>
</main>
</body>
</html>
```